Halvorsen Spa

We are a large Miami Beach spa and salon. I am still building our website but you can use it as a resource to gain a better understanding of who we are ....www.spaquillowave.com.

We offer a comprehensive list of services in hair, nails, massage, skin care, tanning, spray tanning and waxing and we offer high quality products for skin care, tanning and hair. We are open 7 days.

We would like to see a clean and simple menu that looks a lot like the one from "The Spa at Brightmere." In particular, we have a copy of a menu from their West Hollywood, CA location that is just beautiful. In the uploaded content you will see a sampling of that menu. We would like to see greys, blacks, silvers, whites and warm colors like reds and oranges. We specifically attempt to remain gender neutral so that we don't attract only girls (with pink colors and flowers etc). The final design should convey a simple, clean, friendly environment and the final product should be sized such that it is 1.) portable and 2.) inexpensive to print. We will be running thousands of these at a time so cost of printing is a consideration.

The booklet consists of two parts: one part is the standard menu with descriptions of services and products and photos etc (think of this as the sales piece that convinces a potential customer to visit) and will be stapled together like you would expect a small menu to be and should resemble the Brightmere menu. The prices should not be included in this part of the booklet that will be printed and stapled. The other part is a single insert and is removable and replaceable. I want this removable insert placed in the last page of the book in a folder pocket or something else that you can think of so that when it's time to change prices here that I am not throwing away all of the booklets....I am only replacing the inserts at the end of the menu booklet. Please design this single page insert so that should a customer remove it from the booklet and keep it, that it stands alone with our name, logo, website and phone number. This page can and probably will have to be 2 sided.

At the back of the booklet, I also want the polices to be printed in one page (think fine print in any sort of business dealing.)

With regard to the look and feel slider of economical v upmarket...we definitely want to convey we deliver upmarket services at reasonable prices. Think, world class services and products at reasonable, everyday prices.

With regard to the uploaded files:
I uploaded both EPS and TIF formats. The colors in those files are not the palette we want at all. The colors we want use for the circular logo must match the standard colors as depicted in the uploaded file "Halvorsentanrooms"

Target Market(s)

The target market is the average 20-35 year old in Miami Beach that cares about their appearance. The range of clientele is quite diverse.

Industry/Entity Type

Environment

Requirements
Must have
• It must have elegant and simple photographs that relate to the services being offered. We are selling a service set and an environment...so this menu should be reflect that goal. The logo should be repeated often throughout the book but in subtle ways.

Stock photos are fine as long as they don't seem obviously stock.

Should not have
• Nothing buddha like. Nothing themed. It should be all inclusive and not seek to identify with any particular group or gender.

Nothing that fits the stereotype of "Miami Beach." We want to represent ourselves in the same category as the best spas in the world because we moving everything we do in that direction. Think class!

```html
<!DOCTYPE html>
<html lang="en">
<head>
<meta charset="utf-8">
<title>Halvorsen Spa – Threading &amp; Waxing</title>
<link href="https://fonts.googleapis.com/css2?family=Josefin+Sans:wght@200;300;400&family=Open+Sans:wght@400&display=swap" rel="stylesheet">
<style>
  :root {
    --charcoal-light: #4a4a4a;
    --charcoal: #2e2e2e;
    --charcoal-deep: #1f1f1f;
    --white: #ffffff;
    --silver: #a7a7a9;
    --silver-band: rgba(200, 200, 204, 0.55);
    --label-text: #2b2b2b;
    --body-text: #f2f2f2;
    --ghost-white: rgba(255, 255, 255, 0.72);
  }
  * { margin: 0; padding: 0; box-sizing: border-box; }
  html, body {
    width: 1200px; height: 423px; overflow: hidden;
    background: var(--charcoal-deep);
  }
  .spread {
    position: relative; width: 1200px; height: 423px; overflow: hidden;
    background: radial-gradient(ellipse 70% 90% at 62% 45%, var(--charcoal-light) 0%, var(--charcoal) 55%, var(--charcoal-deep) 100%);
    font-family: "Open Sans", sans-serif;
  }
  .spread__shapes { position: absolute; inset: 0; }

  .title-band {
    position: absolute; left: 392px; top: 22px; width: 808px; height: 46px;
    background: linear-gradient(90deg, rgba(180,180,184,0.35) 0%, var(--silver-band) 60%, rgba(210,210,214,0.6) 100%);
    border-top: 1px solid rgba(255,255,255,0.35);
  }
  .title-band__text {
    position: absolute; right: 46px; top: 22px;
    font-family: "Josefin Sans", sans-serif; font-weight: 300;
    font-size: 52px; line-height: 52px; letter-spacing: -1px;
    color: var(--white); white-space: nowrap;
  }

  .cover-title {
    position: absolute; left: 22px; top: 266px;
    font-family: "Josefin Sans", sans-serif; font-weight: 200;
    font-size: 92px; line-height: 76px; letter-spacing: -7px;
    color: var(--ghost-white); white-space: nowrap;
  }

  .brand {
    position: absolute; left: 468px; top: 124px; width: 80px;
    display: flex; flex-direction: column; align-items: center; gap: 5px;
  }
  .brand__dot {
    width: 22px; height: 22px; border-radius: 50%;
    border: 2px solid var(--silver);
  }
  .brand__name {
    font-family: "Josefin Sans", sans-serif; font-weight: 400;
    font-size: 10px; letter-spacing: 1.5px; text-transform: uppercase;
    color: var(--silver); text-align: center; line-height: 1.2;
  }

  .service { position: absolute; left: 636px; width: 258px; }
  .service--threading { top: 138px; }
  .service--waxing { top: 270px; }
  .service__label {
    width: 178px; height: 12px; background: var(--silver);
    font-family: "Josefin Sans", sans-serif; font-weight: 400;
    font-size: 10px; line-height: 13px; letter-spacing: 1.2px;
    color: var(--label-text); text-align: center; text-transform: uppercase;
  }
  .service__text {
    margin-top: 12px;
    font-size: 8px; line-height: 10px; text-align: justify;
    hyphens: auto; -webkit-hyphens: auto;
    color: var(--body-text);
  }
</style>
</head>
<body>
<main class="spread">
  <svg class="spread__shapes" width="1200" height="423" viewBox="0 0 1200 423">
    <defs>
      <linearGradient id="photoTone" x1="0" y1="0" x2="1" y2="1">
        <stop offset="0" stop-color="#d6d4d9"/>
        <stop offset="0.5" stop-color="#c7c4ca"/>
        <stop offset="1" stop-color="#a99c94"/>
      </linearGradient>
      <linearGradient id="tealBand" x1="0" y1="0" x2="0" y2="1">
        <stop offset="0" stop-color="#24596d"/>
        <stop offset="1" stop-color="#143646"/>
      </linearGradient>
    </defs>
    <polygon class="accent-band" points="340,0 392,0 488,423 446,423" fill="url(#tealBand)"/>
    <polygon class="photo-area" role="img"
      aria-label="Photograph of a model in a blue swimsuit seated on a white block, showing smooth skin after hair removal"
      points="0,0 344,0 450,423 0,423" fill="url(#photoTone)"/>
    <circle class="ghost-ring" cx="1128" cy="340" r="76" fill="none" stroke="rgba(160,160,164,0.35)" stroke-width="11"/>
  </svg>

  <div class="title-band"></div>
  <h1 class="title-band__text">THREADING &amp; WAXING</h1>

  <div class="cover-title">THREADING<br>&amp; WAXING</div>

  <div class="brand">
    <span class="brand__dot"></span>
    <span class="brand__name">Halvorsen<br>Spa</span>
  </div>

  <section class="service service--threading">
    <h2 class="service__label">Threading</h2>
    <p class="service__text">Threading is an ancient hair removal technique passed down through the generations in Middle and Far Eastern countries. The technique utilizes only a single cotton thread, masterfully manipulated in the hands of our trained staff, to remove the entire hair follicle from areas of the face. Threading only removes the unwanted hair, without removing the top layer of skin, which is common to traditional waxing. The results can last up to six weeks depending on your hair’s rate of regrowth, and because it uses only a disposable thread, it is perfectly sanitary and entirely chemical-free.</p>
  </section>

  <section class="service service--waxing">
    <h2 class="service__label">Waxing</h2>
    <p class="service__text">Waxing is perhaps the most commonly elected hair removal technique, where thin layers of warm wax are applied to the areas of unwanted hair, allowed to cool encapsulating the hair and the hair is then removed. Unlike threading which is restricted to facial areas, any area of the body can be waxed.</p>
  </section>
</main>
</body>
</html>
```